Promo flyer

Simple, clean flyer to hand to customers during a wedding expo. These will be handed out to foot traffic.
Flyer must be easy to read, simple but pretty and in line with our branding.
Logo must be shown
Images and or styling tools
Please look at our website to get a feel for the brand/colours/etc.
www.larkspurlocks.co.uk
The images attached are samples from the website....something along these lines. Images can be used alone and wording separate.
HD images of the girls alone can be provided so its best quality for print.

Mention
-Shop our luxurious hair extensions & styling tools
-www.larkspurlocks.co.uk
-QT50 = 50% off all styling tools
-Complimentary colour match for hair extensions. Email uk@larkspurlocks.com.

Requirements
Must have
• Logo must be shown
• Images and or styling tools
• BEFORE & AFTER Images (1 before and after) - refer to this link below.
• https://www.larkspurlocks.com/pages/before-afters-see-the-difference
• Please look at our website to get a feel for the brand/colours/etc.
• www.larkspurlocks.co.uk
• The images attached are samples from the website....something along these lines. Images can be used alone and wording separate.
Nice to have
• Water colour behind the discount codes so this stands out

```html
<!DOCTYPE html>
<html lang="en">
<head>
<meta charset="UTF-8">
<title>Larkspur Locks – Promo Flyer</title>
<link href="https://fonts.googleapis.com/css2?family=Open+Sans:ital,wght@0,400;0,600;1,400&family=Oswald:wght@500&display=swap" rel="stylesheet">
<style>
  :root {
    --pink: #f08fbf;
    --pink-soft: #f7d5e5;
    --pink-text: #ec8bbb;
    --plum: #b5489a;
    --white: #ffffff;
    --grey-line: #e3e3e3;
    --label-grey: #e4e4e4;
    --label-text: #7a7a7a;
  }
  * { margin: 0; padding: 0; box-sizing: border-box; }
  html, body { width: 915px; height: 1200px; overflow: hidden; background: var(--white); }
  .flyer {
    position: relative;
    width: 915px;
    height: 1200px;
    overflow: hidden;
    font-family: "Open Sans", Arial, sans-serif;
    background: linear-gradient(to bottom, var(--pink-soft) 0, var(--white) 260px);
  }
  .hero-photo {
    position: absolute;
    left: 38px; top: 0;
    width: 524px; height: 700px;
    background: radial-gradient(ellipse at 48% 35%, #c99a82 0 18%, #4a3230 40%, #2b1f1e 70%, rgba(43,31,30,0) 90%);
  }
  .brand {
    position: absolute;
    left: 566px; top: 88px;
    width: 300px;
    text-align: center;
  }
  .brand-circle {
    width: 176px; height: 176px;
    margin: 0 auto;
    border: 2px solid var(--pink-text);
    border-radius: 50%;
  }
  .brand-name {
    margin-top: 40px;
    color: var(--pink-text);
    font-size: 19px;
    letter-spacing: 4px;
    font-weight: 400;
    white-space: nowrap;
  }
  .waves { position: absolute; left: 0; top: 0; width: 915px; height: 1200px; }
  .headline {
    position: absolute;
    left: 41px; top: 655px;
    width: 560px;
    text-align: center;
    color: var(--white);
    font-size: 29px;
    font-weight: 400;
    line-height: 56px;
    letter-spacing: 0.5px;
    white-space: nowrap;
  }
  .offer-badge {
    position: absolute;
    left: 562px; top: 441px;
    width: 296px; height: 296px;
    border-radius: 50%;
    background: var(--plum);
    border: 9px solid var(--white);
    box-shadow: 0 4px 14px rgba(0,0,0,0.25);
    color: var(--white);
    text-align: center;
    padding-top: 72px;
  }
  .offer-amount { font-family: "Oswald", "Arial Narrow", sans-serif; font-weight: 500; font-size: 64px; line-height: 76px; }
  .offer-item { font-size: 23px; line-height: 30px; margin-top: 6px; }
  .offer-code { font-size: 20px; line-height: 28px; }
  .result-photo {
    position: absolute;
    top: 838px;
    width: 250px; height: 287px;
  }
  .result-photo.before { left: 52px; background: linear-gradient(to bottom, #5a4034 0, #b88e6c 45%, #1e1a1a 80%); }
  .result-photo.after { left: 638px; background: linear-gradient(to bottom, #6b4a36 0, #c79c72 50%, #1e1a1a 85%); }
  .result-label {
    position: absolute;
    top: 1084px;
    width: 126px; height: 28px;
    border-radius: 14px;
    background: var(--label-grey);
    color: var(--label-text);
    font-style: italic;
    font-size: 16px;
    line-height: 28px;
    text-align: center;
    text-transform: uppercase;
  }
  .result-label.before { left: 30px; }
  .result-label.after { left: 622px; }
  .result-claim {
    position: absolute;
    left: 312px; top: 950px;
    width: 312px;
    text-align: center;
    color: var(--pink-text);
    font-size: 24px;
    line-height: 44px;
    text-transform: uppercase;
    white-space: nowrap;
  }
  .colour-match {
    position: absolute;
    left: 312px; top: 1052px;
    width: 312px;
    text-align: center;
    color: var(--pink-text);
    font-size: 14px;
    line-height: 20px;
  }
  .colour-match strong { font-weight: 600; }
  .footer-bar {
    position: absolute;
    left: 0; bottom: 0;
    width: 915px; height: 72px;
    background: var(--pink);
    color: var(--white);
    font-size: 27px;
    line-height: 72px;
    text-align: center;
    letter-spacing: 0.5px;
  }
</style>
</head>
<body>
  <main class="flyer">
    <div class="hero-photo" role="img" aria-label="Model with long dark wavy hair styling it with a rose-gold curling wand"></div>

    <div class="brand">
      <div class="brand-circle"></div>
      <p class="brand-name">LARKSPUR LOCKS</p>
    </div>

    <svg class="waves" viewBox="0 0 915 1200" aria-hidden="true">
      <path d="M0 560 C200 520 420 560 620 640 C740 690 840 700 915 690 L915 720 C830 730 730 715 610 670 C420 595 200 560 0 600 Z" fill="var(--grey-line)"/>
      <path d="M0 490 C180 470 360 500 560 575 C720 635 840 655 915 655 L915 990 C780 930 620 860 430 830 C260 805 110 840 0 890 Z" fill="var(--pink)"/>
      <path d="M0 530 C190 500 400 540 600 620 C740 675 840 690 915 680" fill="none" stroke="var(--white)" stroke-width="14"/>
      <path d="M0 905 C120 850 270 815 430 830 C620 850 780 920 915 1000" fill="none" stroke="var(--white)" stroke-width="10"/>
      <path d="M0 935 C130 875 280 845 440 855 C630 870 790 945 915 1030 L915 1200 L0 1200 Z" fill="var(--white)"/>
      <path d="M0 935 C130 875 280 845 440 855 C630 870 790 945 915 1030" fill="none" stroke="var(--grey-line)" stroke-width="10"/>
    </svg>

    <h1 class="headline">SHOP OUR LUXURIOUS HAIR<br>EXTENSIONS &amp; STYLING TOOLS</h1>

    <div class="offer-badge">
      <p class="offer-amount">50% OFF</p>
      <p class="offer-item">STYLING TOOLS</p>
      <p class="offer-code">use code: QT50</p>
    </div>

    <div class="result-photo before" role="img" aria-label="Before: model with shoulder-length ombré hair"></div>
    <div class="result-photo after" role="img" aria-label="After: same model with long, full, wavy ombré hair extensions"></div>
    <span class="result-label before">Before</span>
    <span class="result-label after">After</span>

    <p class="result-claim">Instantly get longer,<br>thicker hair.</p>
    <p class="colour-match">Complimentary colour match<br>for hair extensions. Email<br><strong>uk@larkspurlocks.com</strong></p>

    <footer class="footer-bar">www.larkspurlocks.co.uk</footer>
  </main>
</body>
</html>
```